Construction Company informative web page

Torvell Builders is a new company that combine Project Manager and kitchen & bath design with Interior remodeling for houses or business (commercial and residential construction)
We want to show our reviews, portafolio and background experience
Updates

Reason: I would like to have the time to interact with the favorite designers to fine tune the website also I'd like to see more designs

Hello Everybody,

Thank you for your time, please make the corrections shown below:

Pages:

1. Home:

1.  Includes a welcome and a briefly background:

2. Right side vertically show a few reviews with the option read more to open it, just the Name and last name, city and review (no start ratings)

3. Facebook and youtube link

4. Left side below shows 4 slides show with pictures and titles:

1. Kitchen Design

2. Bath Design

3. General Remodeling

4. Commercial Projects

2. About Us:

Our Professionals:

Torvell Builders Project Manager  is responsible to set the project schedule, request materials  and coordinate the delivery on time.  The Project Manager focus is ensuring  the best customer satisfaction in every step of the project until the final product is completed.

The Designer gives you the best ideas in 3D format,   getting the best lay out possible.  understanding your needs, defining your unique style putting together all your requirements and ideas to make the best match for you, making sure you get the best products within your budget

Torvell Builders have a high quality group of trade specialist; plumbers, electricians and installers. Our crew is pleasant to work with,  safety and cleaning values  and very detailed oriented

Our Core Values

As our slogan your project is our business, well we really mean it our job is not just to do the job is to guaranteed a pleasant experience with great costumer service, communication, quality, in time and within your budget

 

1. Services:

1. Commercial

2. Residential

2. Portafolio:  Separated pictures in each project, I want to have a brief description in each picture

1. Kitchen Design

2. Bath Design

3. General Remodeling

4. Commercial Projects

 

1. Contact Us:  

1. Project Management Department:

Contact Person: Rhonda Kestling

Email: rhonda@torvellbuilders.com

2. Office Management Department:

Contact Person: Lou Brambery

Email: info@torvellbuilders.com

 

Please try to pick design style shown in business card to match a little bit. Keep the color tones

I want the logo in the upper left corner and a very nice picture with a kitchen (warm colors)mostly American northeast style like the main pic of the web.

I want the web page is able to be fully open in computers, tablets and cellphones

Please send me an email to torvellbuilders1@mailnest.com so I can send you my logo and any other information to be incorporated

Thank you

Hello Everybody,

Thank you for your time, please make the corrections accordingly:

Pages:

1. Home: Includes a welcome and a briefly say something about our background 

Hello, I just upload my logo and my business card so you can adjust your designs

Please presented responsive format

I want coding the webpage too

Please read carefully my last update

Thank you so much!                                   

Industry/Entity Type

Residential

Requirements
Nice to have
• Should it has a Newsletter subscription with the email at the bottom of the home page
In contact page: A box "Contact us for a free estimate"

```html
<!DOCTYPE html>
<html lang="en">
<head>
<meta charset="utf-8">
<title>Torvell Builders</title>
<link href="https://fonts.googleapis.com/css2?family=Questrial&family=Arimo:wght@400;700&family=Open+Sans:wght@600;700&family=Noticia+Text:ital@1&display=swap" rel="stylesheet">
<style>
:root{
  --red:#7b2227;
  --red-dark:#5e1519;
  --red-deep:#681a1e;
  --sand:#e4c48d;
  --sand-light:#efd9ae;
  --paper:#fdfaf3;
  --card:#f3ece1;
  --ink:#3b2c25;
  --muted:#6b5b52;
  --white:#fff;
}
*{box-sizing:border-box;margin:0;padding:0}
html,body{width:1011px;height:1200px;overflow:hidden}
body{background:var(--paper);font-family:"Arimo",Arial,sans-serif;color:var(--ink);position:relative}
.abs{position:absolute}

/* header */
.top-strip{left:0;top:0;width:1011px;height:12px;background:var(--sand)}
.masthead{left:0;top:12px;width:1011px;height:102px;background:var(--red);border-top:3px solid var(--sand-light)}
.logo-disc{left:111px;top:-12px;width:144px;height:144px;border-radius:50%;background:var(--sand);border:4px solid var(--sand-light);display:flex;align-items:center;justify-content:center;text-align:center;z-index:3}
.logo-disc span{font-family:"Questrial",sans-serif;font-size:17px;color:var(--red);line-height:1.15;width:100px}
.brand-name{left:265px;top:48px;font-family:"Questrial",sans-serif;font-size:22px;color:var(--sand);letter-spacing:.3px}
.brand-tag{left:266px;top:76px;font-family:"Questrial",sans-serif;font-size:14px;color:var(--sand)}
.phone{right:110px;top:50px;font-family:"Open Sans",sans-serif;font-weight:700;font-size:14px;color:var(--white);display:flex;align-items:center;gap:6px}
.social{display:flex;gap:4px}
.social i{display:block;width:16px;height:16px;background:var(--sand);border-radius:2px}
.header-social{right:110px;top:84px}

/* nav */
.nav{left:0;top:114px;width:1011px;height:38px;background:var(--sand)}
.nav ul{list-style:none;position:absolute;left:290px;top:0;display:flex;align-items:center;height:38px}
.nav li{font-family:"Open Sans",sans-serif;font-weight:700;font-size:11px;color:var(--red-dark);padding:0 14px;height:30px;line-height:30px;position:relative;z-index:0;white-space:nowrap}
.nav li+li::before{content:"";position:absolute;left:-3px;top:12px;width:6px;height:6px;border-radius:50%;background:var(--red);z-index:1}
.nav li.active{color:var(--sand-light)}
.nav li.active::after{content:"";position:absolute;left:0;right:0;top:-3px;bottom:-7px;background:var(--red);z-index:-1}
.dropdown{left:527px;top:150px;width:166px;background:var(--red);z-index:4;border:1px solid var(--red-dark)}
.dropdown div{font-family:"Open Sans",sans-serif;font-weight:700;font-size:9px;color:var(--sand);padding:0 0 0 16px;height:23px;line-height:23px;border-bottom:1px solid #9a4348;position:relative}
.dropdown div:last-child{border-bottom:0}
.dropdown div::before{content:"";position:absolute;left:8px;top:10px;width:3px;height:3px;border-radius:50%;background:var(--sand)}

/* hero */
.hero{left:0;top:152px;width:1011px;height:280px;background:radial-gradient(ellipse at 30% 35%,#e6a860 0%,#a8622e 35%,#5a2a16 75%,#2b140c 100%)}
.hero-title{left:0;top:344px;width:1011px;text-align:center;color:var(--white);font-size:26px;line-height:28px}
.hero-title .l1{font-family:"Questrial",sans-serif;letter-spacing:.5px}
.hero-title .l2{font-family:"Open Sans",sans-serif;font-weight:700;font-size:25px}
.dots{left:489px;top:412px;display:flex;gap:5px}
.dots i{width:8px;height:8px;border-radius:50%;background:#f0e4d0}
.dots i:first-child{background:#c8322e}

/* main */
.section-title{font-family:"Questrial",sans-serif;font-weight:400;font-size:18px;color:var(--red-dark);padding-bottom:6px;border-bottom:2px solid var(--red);width:141px;white-space:nowrap}
.copy p{font-size:9.3px;line-height:14.7px;color:#4a3a32;margin-bottom:14.7px}
.welcome{left:111px;top:450px;width:512px}
.about{left:111px;top:610px;width:512px}
.btn{display:inline-block;background:var(--red);color:var(--white);font-size:9.5px;padding:0 15px;height:22px;line-height:22px;border:1px solid var(--red-dark)}
.latest{left:111px;top:810px}
.carousel{left:111px;top:858px;width:790px;height:160px}
.arrow{top:48px;width:14px;height:26px}
.work{position:absolute;top:0;width:175px;text-align:center}
.work .shot{height:122px;border:2px solid #e0d6c6}
.work .label{font-family:"Open Sans",sans-serif;font-weight:600;font-size:13px;color:var(--red);margin-top:14px}

/* sidebar */
.estimate{left:650px;top:446px;width:250px;height:49px;background:var(--red);border:3px double var(--sand-light);outline:1px solid var(--red-dark);display:flex;align-items:center;justify-content:space-between;padding:0 10px 0 11px;font-family:"Questrial",sans-serif;font-size:12.5px;color:var(--sand-light)}
.estimate .cta{white-space:nowrap}
.estimate b{font-family:"Open Sans",sans-serif;font-weight:700}
.testimonials{left:650px;top:505px;width:250px;height:237px;background:var(--card);border:2px solid #e4dacb;padding:12px 20px}
.testimonials h3{font-family:"Questrial",sans-serif;font-weight:400;font-size:18px;color:var(--red-dark);margin-top:24px;margin-left:50px}
.quote-mark{left:20px;top:12px}
.testimonials p{font-family:"Noticia Text",serif;font-style:italic;font-size:9.5px;line-height:13.5px;color:#4b3d35;margin-top:12px}
.testimonials .who{font-size:10px;color:var(--red);margin-top:10px}
.testimonials .city{font-size:8.5px;color:var(--muted);margin-top:3px;margin-bottom:10px}
.findus{left:650px;top:752px;width:250px;height:49px;background:var(--red);border:3px double var(--sand-light);outline:1px solid var(--red-dark);display:flex;align-items:center;justify-content:center;gap:10px;font-family:"Questrial",sans-serif;font-size:16px;color:var(--sand-light)}
.findus .cta{white-space:nowrap}
.findus b{font-family:"Open Sans",sans-serif}
.findus i{display:block;width:23px;height:23px;background:var(--sand);border-radius:3px}

/* footer */
.footer{left:0;top:1027px;width:1011px;height:136px;background:var(--red);border-top:3px solid #eee3d4}
.foot-logo{left:111px;top:1038px;width:76px;height:76px;border-radius:50%;background:var(--sand);display:flex;align-items:center;justify-content:center;text-align:center}
.foot-logo span{font-family:"Questrial",sans-serif;font-size:10px;color:var(--red);width:56px;line-height:1.15}
.foot-name{left:196px;top:1066px;font-family:"Questrial",sans-serif;font-size:15.5px;color:var(--sand-light)}
.foot-tag{left:196px;top:1085px;font-family:"Questrial",sans-serif;font-size:10.5px;color:var(--sand)}
.foot-contact{left:196px;top:1106px;font-size:10px;color:var(--sand-light);line-height:21px}
.foot-contact div{display:flex;align-items:center;gap:13px}
.foot-find{right:110px;top:1047px;display:flex;align-items:center;gap:6px;font-family:"Noticia Text",serif;font-style:italic;font-size:10px;color:var(--sand)}
.newsletter-title{right:110px;top:1076px;font-size:12px;color:var(--sand-light)}
.newsletter{right:110px;top:1098px;width:182px;height:21px;background:#fbf6ec;border:1px solid var(--sand);display:flex}
.newsletter span{flex:1;font-family:"Noticia Text",serif;font-style:italic;font-size:9.5px;color:#6d5f55;line-height:19px;padding-left:8px}
.newsletter i{width:21px;background:var(--red);display:flex;align-items:center;justify-content:center;border-left:1px solid var(--sand)}
.foot-links{right:110px;top:1135px;font-size:10px;color:var(--sand-light)}
.foot-links span{margin:0 5px;color:var(--sand)}
.copyright{left:0;top:1163px;width:1011px;height:37px;background:var(--red-dark);text-align:center;line-height:37px;font-size:8.5px;color:var(--sand)}
</style>
</head>
<body>

<div class="abs top-strip"></div>
<header class="abs masthead"></header>
<div class="abs logo-disc"><span>Torvell Builders</span></div>
<div class="abs brand-name">TORVELL BUILDERS</div>
<div class="abs brand-tag">Your project is our business</div>
<div class="abs phone">
  <svg width="11" height="11" viewBox="0 0 24 24"><path fill="#fff" d="M6.6 10.8a15 15 0 0 0 6.6 6.6l2.2-2.2c.3-.3.7-.4 1-.2 1.1.4 2.3.6 3.6.6.6 0 1 .4 1 1V20c0 .6-.4 1-1 1A17 17 0 0 1 3 4c0-.6.4-1 1-1h3.5c.6 0 1 .4 1 1 0 1.3.2 2.5.6 3.6.1.3 0 .7-.2 1z"/></svg>
  555-014-2730
</div>
<div class="abs social header-social"><i></i><i></i><i></i><i></i><i></i></div>

<nav class="abs nav">
  <ul>
    <li>HOME</li>
    <li>ABOUT US</li>
    <li>SERVICES</li>
    <li class="active">PORTAFOLIO</li>
    <li>CONTACT US</li>
  </ul>
</nav>
<div class="abs dropdown">
  <div>KITCHEN DESIGN</div>
  <div>BATH DESIGN</div>
  <div>GENERAL REMODELING</div>
  <div>COMMERCIAL PROJECTS</div>
</div>

<div class="abs hero" role="img" aria-label="Warm-toned kitchen with wooden cabinets, tiled backsplash and granite counters"></div>
<div class="abs hero-title">
  <div class="l1">COMMERCIAL &amp; RESIDENTIAL GENERAL</div>
  <div class="l2">CONSTRUCTION KITCHEN &amp; BATH DESIGN</div>
</div>
<div class="abs dots"><i></i><i></i><i></i></div>

<section class="abs welcome copy">
  <h2 class="section-title">WELCOME</h2>
  <p style="margin-top:12px">Lorem ipsum dolor sit amet, consectetur adipiscing elit. Ut sit amet metus ut lorem pharetra venenatis fermentum at nibh. Nulla aliquet diam eu turpis convallis sit amet malesuada mi ultrices.</p>
  <p>In in velit massa, vitae condimentum leo. Vivamus nulla sapien, bibendum eget malesuada eget, volutpat nec nisl. Aenean turpis magna, dapibus a laoreet a, eleifend eget metus. Vestibulum quis interdum lacus. Vivamus nulla sapien, bibendum eget malesuada eget, volutpat nec nisl. Aenean turpis magna, dapibus a laoreet. Livamus nulla sapien, bibendum eget malesuada eget, volutpat nec nisl. Aenean turpis magna, dapibus a laoreet.</p>
</section>

<section class="abs about copy">
  <h2 class="section-title">ABOUT US</h2>
  <p style="margin-top:12px">Torvell Builders Project Manager is responsible to set the project schedule, request materials and coordinate the delivery on time. The Project Manager focus is ensuring the best customer satisfaction in every step of the project until the final product is completed.</p>
  <p>The Designer gives you the best ideas in 3D format, getting the best lay out possible. understanding your needs, defining your unique style putting together all your requirements and ideas to make the best match for you, making sure you get the best products within your budget.</p>
  <span class="btn">Read More</span>
</section>

<h2 class="abs section-title latest">LATEST WORK</h2>
<div class="abs carousel">
  <svg class="abs arrow" style="left:0" viewBox="0 0 14 26"><path d="M12 2 2 13l10 11" fill="none" stroke="#d6cbbb" stroke-width="3"/></svg>
  <div class="work" style="left:21px"><div class="shot" role="img" aria-label="Kitchen design project" style="background:linear-gradient(160deg,#c98a4c,#6b3a1e)"></div><div class="label">Kitchen Design</div></div>
  <div class="work" style="left:212px"><div class="shot" role="img" aria-label="Bath design project" style="background:linear-gradient(160deg,#e9e6dc,#a8a596)"></div><div class="label">Bath Design</div></div>
  <div class="work" style="left:403px"><div class="shot" role="img" aria-label="General remodeling project" style="background:linear-gradient(160deg,#e2b57e,#8c4a28)"></div><div class="label">General Remodeling</div></div>
  <div class="work" style="left:594px"><div class="shot" role="img" aria-label="Commercial project" style="background:linear-gradient(160deg,#8f8a82,#e8e6e1)"></div><div class="label">Commercial Projects</div></div>
  <svg class="abs arrow" style="left:776px" viewBox="0 0 14 26"><path d="M2 2l10 11L2 24" fill="none" stroke="#d6cbbb" stroke-width="3"/></svg>
</div>

<aside>
  <div class="abs estimate"><span class="cta">CONTACT US FOR A <b>FREE ESTIMATE</b></span>
    <svg width="24" height="22" viewBox="0 0 24 22"><path d="M2 2h20v14H10l-5 5v-5H2z" fill="var(--sand-light)"/><path d="M6 7h12M6 11h9" stroke="var(--red)" stroke-width="1.6"/></svg>
  </div>
  <div class="abs testimonials">
    <svg class="abs quote-mark" width="48" height="36" viewBox="0 0 48 36"><path d="M4 36V16C4 6 9 2 18 1v7c-4 1-6 4-6 8h6v20zM28 36V16c0-10 5-14 14-15v7c-4 1-6 4-6 8h6v20z" fill="#dccfbe"/></svg>
    <h3>TESTIMONIALS</h3>
    <p>Lorem ipsum dolor sit amet, consectetur adipi-scing elit. Ut sit amet metus ut lorem.</p>
    <p>Pharetra venenatis fermentum at nibh. Nulla aliquet diam eu turpis convallis sit amet male-suada mi ultrices. Nulla aliquet diam eu turpis convallis sit amet malesuada mi ultrices.</p>
    <div class="who">Dana Whitlow</div>
    <div class="city">New York</div>
    <span class="btn">Read More</span>
  </div>
  <div class="abs findus"><span class="cta">FIND <b>US ON</b></span> <i></i><i></i></div>
</aside>

<footer class="abs footer"></footer>
<div class="abs foot-logo"><span>Torvell Builders</span></div>
<div class="abs foot-name">TORVELL BUILDERS</div>
<div class="abs foot-tag">Your project is our business</div>
<div class="abs foot-contact">
  <div><svg width="10" height="10" viewBox="0 0 24 24"><path fill="var(--sand)" d="M6.6 10.8a15 15 0 0 0 6.6 6.6l2.2-2.2c.3-.3.7-.4 1-.2 1.1.4 2.3.6 3.6.6.6 0 1 .4 1 1V20c0 .6-.4 1-1 1A17 17 0 0 1 3 4c0-.6.4-1 1-1h3.5c.6 0 1 .4 1 1 0 1.3.2 2.5.6 3.6.1.3 0 .7-.2 1z"/></svg>555-014-2730</div>
  <div><svg width="11" height="9" viewBox="0 0 22 16"><rect width="22" height="16" fill="var(--sand)"/><path d="M1 1l10 8 10-8" fill="none" stroke="var(--red)" stroke-width="1.8"/></svg>info@torvellbuilders.com</div>
</div>
<div class="abs foot-find">Find us on <span class="social"><i></i><i></i><i></i><i></i><i></i></span></div>
<div class="abs newsletter-title">Newsletter Subscription</div>
<div class="abs newsletter"><span>Enter Your Email</span><i><svg width="7" height="10" viewBox="0 0 7 10"><path d="M1 1l4 4-4 4" fill="none" stroke="#fff" stroke-width="1.6"/></svg></i></div>
<div class="abs foot-links">Home<span>|</span>About Us<span>|</span>Services<span>|</span>Portafolio<span>|</span>Contact Us</div>
<div class="abs copyright">Copyright © 2014 torvellbuilders.com. All Rights Reserved.</div>

</body>
</html>
```